New Brochure Design Project *

I am in need of a brochure design/layout that 'Wows' prospective customers and provides essential information about our company.
The name of the Company is Rolly Dex Charter Fishing Service.
Located in Port Washington, Wisconsin.
We take customers fishing on Lake Michigan . We have been in business for over 30 years with a reputation for the most successful fishing charter in the area. Voted best fishing Charter for several years in a row. We fish for Chinook Salmon, Steelhead, Brown Trout, Coho Salmon and Lake Trout. Our fleet of 4 large fishing boats are well maintained and fully equipped with all fishing tackle , the latest in fishing gear and electronics, private restroom, heat and air. Fully insured. Our boats are U.S. Coast Guard Certified and licensed to accommodate 1 to 6 passengers.
Our selected Captains have over 100 years of experience fishing Lake Michigan .
Target market: Corporations that provide team building exercises,/ rewards employees for a job well done/ entertain clients, Outdoor enthusiasts, Men, women and families that enjoy fresh water fishing.
Design specifics: I would like to have 5-7 photos of our catch, ( I can provide those ) photos of the 4 boats ( I will provide ) Our Logo ( I will provide ) A page for our rates and packages, our website, contact information.
Our current brochure can be viewed on our website under the downloadable brochure tab. At www.rollydexcharters.example Our FaceSpace www.facebook.com/RollyDexChartersLLC page is a great way to learn more about us as well and responses from our customers plus reviews of our Company for reference. I am open to advice on this project.
Our current brochure is a colored two sided brochure with 5 panels that fold up ( almost accordion style ) with a front and back cover. I am open to new layouts and easier folding options.
Attached is our logo, and current brochure. I will send photos as needed.( I will be making price adjustments for the new brochure)
Thank you so much for your help.

```html
<!DOCTYPE html>
<html lang="en">
<head>
<meta charset="utf-8">
<title>Rolly Dex Charter Fishing Service – Brochure Inside</title>
<link href="https://fonts.googleapis.com/css2?family=Oswald:wght@400;500;600&family=Roboto+Condensed:wght@400;700&display=swap" rel="stylesheet">
<style>
:root{
  --navy:#163a86;
  --ink:#1b2f5c;
  --sky-top:#eef4fa;
  --sky-mid:#d9e6f2;
  --water:#aecbe3;
  --water-deep:#8fb5d6;
  --white:#ffffff;
  --photo-a:#7f9fbf;
  --photo-b:#c9d7e4;
}
*{box-sizing:border-box;margin:0;padding:0}
html,body{width:1200px;height:504px;overflow:hidden;background:var(--white)}
.brochure{position:relative;width:1200px;height:504px;overflow:hidden;
  background:linear-gradient(180deg,var(--sky-top) 0%,var(--sky-mid) 38%,var(--water) 60%,var(--water-deep) 100%);
  font-family:"Roboto Condensed",sans-serif;color:var(--ink);font-size:8.3px;line-height:1.4}
.abs{position:absolute}
h2{font-family:"Oswald",sans-serif;font-weight:500;color:var(--navy);line-height:1.15}
.photo{position:absolute;border:4px solid var(--white);box-shadow:0 1px 4px rgba(0,0,0,.25);
  background:linear-gradient(160deg,var(--photo-b),var(--photo-a))}
.boat-photo{background:linear-gradient(180deg,#dbe7f1 0%,#c3d6e7 45%,#6f9cc4 46%,#4f7fae 100%)}
.tag{position:absolute;background:var(--navy);color:var(--white);font-family:"Oswald",sans-serif;
  font-size:12px;padding:2px 6px;white-space:nowrap}
.intro-head{left:6px;top:14px;width:230px;font-size:13px;text-align:center}
.badge{left:152px;top:130px;width:84px;height:84px;border-radius:50%;background:var(--navy);
  border:3px solid var(--white);color:var(--white);font-family:"Oswald",sans-serif;text-align:center;
  display:flex;flex-direction:column;justify-content:center;line-height:1;transform:rotate(-6deg)}
.badge b{font-weight:500;font-size:15px}
.badge span{font-size:9.5px}
.captains{left:26px;top:218px;width:196px}
.captains p{margin-bottom:6px}
.list-head{font-weight:700;margin-bottom:4px}
ul.bullets{list-style:none}
ul.bullets li{position:relative;padding-left:10px;margin-bottom:4px}
ul.bullets li::before{content:"";position:absolute;left:1px;top:5px;width:3px;height:3px;border-radius:50%;background:var(--ink)}
.fine{left:26px;top:472px;width:180px;font-size:4px;line-height:1.3}
.fleet{left:262px;top:20px;width:186px}
.come{left:294px;top:458px;font-size:21px;font-family:"Oswald",sans-serif;font-weight:600;color:var(--navy)}
.band-title{color:var(--white);font-family:"Oswald",sans-serif;font-size:15px;top:30px}
.calendar{left:505px;top:79px;width:190px}
.season{border-bottom:1px solid rgba(27,47,92,.35);padding-bottom:7px;margin-bottom:9px}
.season:last-child{border-bottom:0}
.season h3{font-size:8.3px;font-weight:700;margin-bottom:3px}
.packages{left:749px;top:79px;width:192px}
.pack{border-bottom:1px solid rgba(27,47,92,.35);padding-bottom:7px;margin-bottom:8px}
.pack:last-child{border-bottom:0}
.pack h3{font-size:8.3px;font-weight:700;margin-bottom:3px}
.rate{display:flex;justify-content:space-between;width:122px}
.join{left:968px;top:278px;width:220px;text-align:center;font-size:28px;font-weight:600;line-height:1.08}
.contact{top:350px;text-align:center;font-size:7.6px;line-height:1.35}
.contact b{display:block}
.fee{left:984px;top:405px;width:104px;font-size:5.6px;text-align:center;line-height:1.25}
.card-name{position:absolute;top:408px;height:18px;width:34px;text-align:center;background:var(--white);border:1px solid var(--navy);
  color:var(--navy);font-weight:700;font-size:6.4px;line-height:16px}
.follow{left:990px;top:432px;font-weight:700;font-size:7.8px;display:flex;gap:7px;align-items:center}
.follow span{color:var(--navy)}
.toll{right:30px;top:462px;text-align:right;color:var(--white);line-height:1.1}
.toll small{font-size:8.5px;display:block}
.toll strong{font-family:"Oswald",sans-serif;font-size:18px;font-weight:500}
</style>
</head>
<body>
<main class="brochure">

  <svg class="abs" style="left:0;top:0" width="1200" height="504" aria-hidden="true">
    <polygon points="474,20 948,24 948,62 560,62 508,58 478,62" fill="var(--navy)"/>
    <polygon points="720,504 1200,444 1200,504" fill="var(--navy)"/>
  </svg>

  <h2 class="abs intro-head">Four Full Time Professional Captains<br>With 102 Years of Combined Experience</h2>
  <div class="photo" role="img" aria-label="Captains and crew posing on deck with their catch of salmon" style="left:16px;top:62px;width:196px;height:126px;transform:rotate(-1.5deg)"></div>
  <div class="abs badge"><b>OVER<br>30 YEARS</b><span>IN BUSINESS!</span></div>

  <section class="abs captains">
    <p>We take pride in our boats and our business. Rolly Dex's selected Captains are the key to a successful fishing trip.</p>
    <p class="list-head">These include:</p>
    <ul class="bullets">
      <li><b>Captain Dan Harlow</b>, 37 years as a licensed Captain on Lake Michigan.</li>
      <li><b>Captain Mike Vernal</b>, 24 years as a licensed Captain on Lake Michigan.</li>
      <li><b>Captain Tom Ardell</b>, 14 years as a licensed Captain with over 25 years fishing experience on Lake Michigan.</li>
      <li><b>Captain Kyle Renner</b>, 12 years as a licensed Captain with over 18 years fishing experience on Lake Michigan.</li>
    </ul>
    <p class="list-head" style="margin-top:8px">Boat Furnishing</p>
    <ul class="bullets">
      <li>All Fishing Tackle</li>
      <li>The Latest in Fishing Gear and Electronics</li>
      <li>Private Restroom, Heat &amp; Air</li>
      <li>Fully Insured</li>
    </ul>
  </section>
  <p class="abs fine">Member of the local harbor chamber and the area charter captains group. All Captains are enrolled in the regional safety consortium.</p>

  <p class="abs fleet">All of our boats are U.S. Coast Guard Certified and licensed to accommodate 1 of 6 passengers.<br><br>
  The “<b>Rolly Dex</b>” is an extra wide 35 foot Harborline Sport Fisherman, accommodating up to six anglers very comfortably. “<b>Rolly Dex II</b>” is sleek, 34 foot Wavecrest Sport Fisherman outfitted with the latest in sport fishing gear. “<b>Rolly Dex III &amp; IV</b>” are 36 foot long, 14 foot wide Baymark, that accommodates 6 fisherman with ease. Either choice promises a great day on the water.</p>

  <div class="photo boat-photo" role="img" aria-label="Charter boat Rolly Dex on the lake" style="left:248px;top:136px;width:196px;height:76px"></div>
  <div class="tag" style="left:392px;top:132px">Rolly Dex</div>
  <div class="photo boat-photo" role="img" aria-label="Charter boat Rolly Dex II docked at the pier" style="left:266px;top:214px;width:198px;height:76px"></div>
  <div class="tag" style="left:248px;top:224px">Rolly Dex II</div>
  <div class="photo boat-photo" role="img" aria-label="Charter boat Rolly Dex III cruising" style="left:248px;top:294px;width:212px;height:76px"></div>
  <div class="tag" style="left:398px;top:302px">Rolly Dex III</div>
  <div class="photo boat-photo" role="img" aria-label="Charter boat Rolly Dex IV under way" style="left:266px;top:372px;width:198px;height:76px"></div>
  <div class="tag" style="left:248px;top:384px">Rolly Dex IV</div>
  <div class="abs come">COME ABOARD!</div>

  <div class="abs band-title" style="left:506px">FISHING SEASON Calendar</div>
  <section class="abs calendar">
    <div class="season"><h3>April 15th thru May 30th</h3>Kick start the season targeting Brown Trout, Lake Trout, and Steelhead. One of the best opportunities for Trophy size Brown and Lake Trout.<br>Book early. These dates fill up fast.</div>
    <div class="season"><h3>June 1st thru June 30th</h3>June is the month for abundant catches of Large Steelhead and Coho Salmon. We leave from our picturesque home harbor for hours of spectacular fun and productive fishing.</div>
    <div class="season"><h3>July 1st thru July 31st</h3>The best King Salmon fishing on Lake Michigan, the place to be is with “Rolly Dex” as we leave from the harbor. The “Kings” range from the 20 to 30 pound class. Intermixed with the “Kings”, prepare to experience some terrific Large Steelhead and Coho Salmon action.</div>
    <div class="season"><h3>August 1st thru August 31st</h3>What a month! Catches of 15 to 20 fish per trip are common from our harbor. Our main target during this period is the fantastic King Salmon. These beauties can range up to 30 pounds plus.</div>
    <div class="season"><h3>September 1st thru October 15th</h3>With the arrival of Fall the King Salmon have the peak of their weight class and moving to the shallower water of the harbor and shoreline to spawn. We go out to harvest the large “Kings” in the early to late morning. Later we move off shore for a variety of two and three year old Salmon. Brown Trout are also on our radar, reaching weights of up to 30 pounds.</div>
  </section>

  <div class="abs band-title" style="left:748px">PACKAGES &amp; RATES</div>
  <section class="abs packages">
    <div class="pack"><h3>Fisherman's Special</h3>3 - Five Hour Charters<br>Two Nights Lodging<br>All Licenses and Trout Stamps (2 day only)<br>For 4 - $526pp | For 5 - $436pp | For 6 - $365pp<br>Required Deposit $600</div>
    <div class="pack"><h3>Captains Special</h3>2 - Six Hour Charters<br>Six Hours of Afternoon Fishing<br>Six Hours Sunrise Fishing<br>All Licenses and Trout Stamps<br>One Night Lodging<br>For 4 - $389pp | For 5 - $314pp | For 6 - $264pp<br>Required Deposit $400</div>
    <div class="pack"><h3>Chinook &amp; Coho Special</h3>2 - Five Hour Charters<br>Five Hours of Afternoon Fishing<br>Five Hours Sunrise Fishing<br>All Licenses and Trout Stamps<br>One Night Lodging<br>For 4 - $349pp | For 5 - $282pp | For 6 - $238pp<br>Required Deposit $350</div>
    <div class="pack"><h3>Half Day Rates</h3>(up to 6 persons maximum, plus tax)
      <div class="rate"><span>5 Hours ...............................</span><span>$570</span></div>
      <div class="rate"><span>6 Hours ...............................</span><span>$650</span></div>
      <div class="rate"><span>7 Hours ...............................</span><span>$730</span></div>
    </div>
  </section>

  <div class="photo" role="img" aria-label="Large group of anglers on the dock behind rows of caught salmon" style="left:954px;top:14px;width:224px;height:250px;transform:rotate(1.5deg)"></div>
  <h2 class="abs join">JOIN US FOR YOUR NEXT ADVENTURE!</h2>
  <div class="abs contact" style="left:980px;width:116px"><b>Gift Certificates Available</b>P.O. Box 412<br>Gullhaven, WI 00000-0412<br>www.rollydexcharters.example</div>
  <div class="abs contact" style="left:1094px;width:84px"><b>Reservation Only</b>1-800-555-0142<br>Office: 1-262-555-0190</div>
  <p class="abs fee">A 3% convenience fee will be added for payments made by credit card.</p>
  <div class="card-name" style="left:1097px">Lakecard</div>
  <div class="card-name" style="left:1134px">Tidecard</div>
  <div class="abs follow">Follow us on <span>FaceSpace</span><span>Chirper</span></div>
  <div class="abs toll"><small>Dial Toll Free</small><strong>1-800-555-0142</strong></div>

</main>
</body>
</html>
```